Home page web design for a lawn specialist business

-The design must be based around the attached HPID (home page information design) called Turf Tidings HPID. I've attached Word and PDF versions - these are the same. The table boxes are just for approximate placement of information and you can use boxes and bold shapes for this design.

All fonts used in the HPID are only examples - you can use any Google font you wish.

- Text that is in orange is for your information only. Text to go on the design is black. Some instructions are in the HPID. Please be creative!

-The design needs to be modern and exciting - colours are to be the green of the logo, and white ...and then choose dark green, or dark grey or black.

Logo - attached (it's not great quality but don't worry, we'll replace it later)

- I've provided the images for the galleries - they are labelled and will match the name in the HPID. Please use the supplied images!

- Examples of some websites that have great design... don't copy them please but they are similar in look to what we are after....
www.qmbbuildworks.co.nz
http://www.rim-safeguard.co.nz/
http://www.lumenhomes.wb.gs/

Important: Width of content will be 1280 pixels when implemented as a web page but the winning design will need to supplied be on a 2000 pixel wide background so nav bars and background can extend outside the 1280 width.
Header height (without nav bar) 150-160 pixels.

We don't comment on individual designs but will choose a winning design promptly.

Industry/Entity Type

Business

Number of Pages Required

1 page

Font styles to use
Sans Serif

Requirements
Must have
• clean, modern, well-spaced design

```html
<!DOCTYPE html>
<html lang="en">
<head>
<meta charset="utf-8">
<title>Turf Tidings – Lawn Specialists</title>
<link href="https://fonts.googleapis.com/css2?family=Open+Sans:wght@400;600;700;800&family=Oswald:wght@500;600&display=swap" rel="stylesheet">
<style>
:root{
  --green:#3f9e1d;
  --green-light:#6cc12f;
  --green-dark:#1d5a0c;
  --ink:#222;
  --muted:#666;
  --panel:#f3f3f3;
  --line:#dcdcdc;
  --footer:#2b2b2b;
  --footer-text:#bdbdbd;
  --white:#fff;
}
*{box-sizing:border-box;margin:0;padding:0}
html,body{width:745px;height:1200px;overflow:hidden;background:var(--white);font-family:"Open Sans",Arial,sans-serif;color:var(--ink)}
.page{position:relative;width:745px;height:1200px}
.wrap{width:455px;margin:0 auto;position:relative}

/* header */
.site-header{height:56px}
.site-header .wrap{display:flex;justify-content:space-between;align-items:center;height:56px}
.brand{display:flex;align-items:center;gap:6px}
.brand-square{width:16px;height:16px;background:var(--green)}
.brand-name{font-weight:800;font-size:15px;color:var(--green)}
.contact{text-align:right}
.contact .tag{font-family:"Oswald",sans-serif;font-weight:600;font-size:15px;letter-spacing:.5px}
.contact .sub{font-size:6.5px;color:var(--muted);line-height:1.25}
.contact .phone{font-family:"Oswald",sans-serif;font-size:17px;font-weight:500;color:var(--ink)}

/* nav */
.main-nav{height:20px;background:linear-gradient(var(--green),var(--green-dark))}
.main-nav ul{list-style:none;display:flex;height:20px;align-items:center;gap:0}
.main-nav li{font-size:6px;font-weight:700;color:var(--white);padding:0 7px;text-transform:uppercase;border-right:1px solid rgba(255,255,255,.25);line-height:20px}
.main-nav li.active{background:var(--green-dark)}

/* hero */
.hero{height:104px;background:linear-gradient(var(--green),var(--green-dark))}
.hero .wrap{padding-top:8px}
.hero-photos{display:flex;justify-content:space-between;padding:0 22px}
.hero-photo{position:relative;width:198px;height:70px;border:2px solid var(--white)}
.photo-before{background:linear-gradient(135deg,#8a9a86,#4a6a5a 55%,#2f4a3c)}
.photo-after{background:linear-gradient(135deg,#9ed05e,#5fa52c 60%,#3e7c1c)}
.hero-label{position:absolute;bottom:4px;left:50%;transform:translateX(-50%);background:rgba(0,0,0,.7);color:var(--white);font-size:8px;padding:2px 12px}
.hero-caption{text-align:center;color:var(--white);font-size:8.5px;font-weight:700;margin-top:7px;letter-spacing:.3px}

/* intro */
.intro{padding:10px 0 0;height:92px;text-align:center}
.intro h1{font-size:10px;font-weight:700}
.intro h2{font-size:8.5px;font-weight:700;margin-top:1px}
.intro p{font-size:5.5px;color:var(--muted);line-height:1.5;text-align:left;margin-top:7px}

/* feature grid */
.feature-grid{display:grid;grid-template-columns:1fr 1fr;gap:8px 11px}
.feature{background:var(--panel);border:1px solid var(--line);height:140px;position:relative}
.feature-tab{display:flex;justify-content:space-between;align-items:center;background:linear-gradient(var(--green-light),var(--green));color:var(--white);font-size:7px;font-weight:700;text-transform:uppercase;height:17px;padding:0 6px}
.feature-photo{margin:6px;height:68px}
.feature p{font-size:5.5px;color:var(--muted);line-height:1.5;margin:0 7px}
.more{position:absolute;right:6px;bottom:6px;background:var(--green);color:var(--white);font-size:6px;font-weight:700;padding:2px 8px}

/* video */
.video-row{display:flex;gap:11px;margin-top:10px;height:156px}
.video{width:222px;background:var(--panel);border:1px solid var(--line)}
.video-frame{margin:6px;height:110px;background:linear-gradient(135deg,#7bb54a,#3f7d22);position:relative}
.video-bar{position:absolute;left:0;right:0;bottom:0;height:10px;background:rgba(0,0,0,.6)}
.about{width:222px;padding-top:4px}
.about h3{font-size:9px;font-weight:800;color:var(--ink);margin-bottom:5px}
.about p{font-size:5.5px;color:var(--muted);line-height:1.5;margin-bottom:5px}

/* testimonial */
.testimonial{position:relative;height:148px;margin-top:8px}
.testimonial h3{font-size:9px;font-weight:800;margin-bottom:4px}
.quote-box{display:flex;gap:8px;width:250px;border:1px solid var(--line);background:var(--white);padding:8px;height:70px}
.quote-mark{font-family:Georgia,serif;font-size:22px;color:var(--green);line-height:1}
.avatar{width:30px;height:34px;background:linear-gradient(#c9c9c9,#a7a7a7);flex:none}
.quote-box p{font-size:5.5px;color:var(--muted);line-height:1.5}
.quote-box .who{font-weight:700;color:var(--ink);margin-top:2px}
.mower{position:absolute;right:-60px;top:0;width:245px;height:148px;background:linear-gradient(120deg,#fff 10%,#cfd3cf 45%,#6f766f 70%,#3f9e1d)}

/* grass band */
.grass{height:102px;background:linear-gradient(#fff 0%,#d9f0c4 30%,#6cc12f 65%,#2f7a12 100%)}

/* footer */
.site-footer{height:210px;background:var(--footer);padding-top:14px}
.site-footer .wrap{display:flex;justify-content:space-between}
.footer-links{list-style:none;width:110px}
.footer-links li{font-size:6px;color:var(--footer-text);line-height:1.55;text-transform:uppercase}
.footer-brand{width:80px;height:80px;background:var(--white);display:flex;flex-direction:column;align-items:center;justify-content:center;gap:5px}
.footer-brand .brand-name{font-size:10px}
.quote-form{width:175px}
.quote-form h4{font-size:9px;color:var(--white);font-weight:700;line-height:1.25}
.quote-form .note{font-size:6px;color:var(--footer-text);margin:2px 0 6px}
.form-row{display:flex;gap:4px;margin-bottom:4px}
.field{flex:1;height:11px;background:var(--white)}
.field.tall{height:30px}
.send{width:30px;background:var(--green);color:var(--white);font-size:6px;font-weight:700;display:flex;align-items:center;justify-content:center}
.copyright{position:absolute;left:0;right:0;bottom:12px;text-align:center;font-size:5.5px;color:#888}
</style>
</head>
<body>
<div class="page">

  <header class="site-header">
    <div class="wrap">
      <div class="brand"><span class="brand-square"></span><span class="brand-name">Turf Tidings</span></div>
      <div class="contact">
        <div class="tag">LAWN SPECIALISTS</div>
        <div class="sub">from ground preparation to Lawncare<br>Servicing The Auckland region</div>
        <div class="phone">0 800 12 34 56</div>
      </div>
    </div>
  </header>

  <nav class="main-nav">
    <div class="wrap">
      <ul>
        <li class="active">Home</li><li>About Us</li><li>Services</li><li>Lawn Care</li><li>Grass Seeding</li><li>Hydroseeding</li><li>FAQs</li><li>Before &amp; After</li><li>Quote</li>
      </ul>
    </div>
  </nav>

  <section class="hero">
    <div class="wrap">
      <div class="hero-photos">
        <div class="hero-photo photo-before" role="img" aria-label="Bare prepared ground before lawn seeding"><span class="hero-label">Before</span></div>
        <div class="hero-photo photo-after" role="img" aria-label="Lush green lawn after seeding"><span class="hero-label">After</span></div>
      </div>
      <div class="hero-caption">LOREM IPSUM DOLOR SIT AMET, CONSECTETEUR ADIPISCING ELIT</div>
    </div>
  </section>

  <section class="intro">
    <div class="wrap">
      <h1>You can always spot an Turf Tidings lawn.</h1>
      <h2>It's the one that turns your neighbours green with envy.</h2>
      <p>If you want a beautiful lawn that stays green all year round, talk to us. We prepare the ground, sow quality seed and care for your new lawn until it is thriving. Our team knows local soils and climate, so every lawn we create is built to last and easy to look after.</p>
      <p>From small gardens to large properties, we offer seeding, hydroseeding and ongoing maintenance. Call us today for a free quote and friendly advice on your lawn.</p>
    </div>
  </section>

  <div class="wrap">
    <div class="feature-grid">
      <article class="feature">
        <div class="feature-tab">Grass Seeding Service<span>›</span></div>
        <div class="feature-photo" role="img" aria-label="Freshly seeded lawn" style="background:linear-gradient(135deg,#a8c98a,#5a8a3a)"></div>
        <p>We prepare your soil and sow premium seed blends for a thick, even lawn that suits your site.</p>
        <span class="more">more</span>
      </article>
      <article class="feature">
        <div class="feature-tab">Lawn Care Maintenance<span>›</span></div>
        <div class="feature-photo" role="img" aria-label="Well kept green lawn" style="background:linear-gradient(135deg,#8fcf55,#3f8a1e)"></div>
        <p>Regular mowing, feeding and weed control to keep your lawn healthy and green all year.</p>
        <span class="more">more</span>
      </article>
      <article class="feature">
        <div class="feature-tab">FAQs About Grass Seeding &amp; Lawn Care<span>›</span></div>
        <div class="feature-photo" role="img" aria-label="Lawn beside a garden path" style="background:linear-gradient(135deg,#6fae3c,#2f6a18)"></div>
        <p>Answers to common questions on seed choice, watering, timing and first mowing.</p>
        <span class="more">more</span>
      </article>
      <article class="feature">
        <div class="feature-tab">Before &amp; After Lawn Photos<span>›</span></div>
        <div class="feature-photo" role="img" aria-label="Garden lawn transformation" style="background:linear-gradient(135deg,#b5d88f,#4f9a2a)"></div>
        <p>See how bare ground turns into a lush lawn with our proven process.</p>
        <span class="more">more</span>
      </article>
    </div>

    <div class="video-row">
      <div class="video">
        <div class="feature-tab">Watch Video On How Turf Tidings Excellent Work<span>›</span></div>
        <div class="video-frame" role="img" aria-label="Video of lawn seeding work"><div class="video-bar"></div></div>
      </div>
      <div class="about">
        <h3>TURF TIDINGS</h3>
        <p>For over ten years we have created lawns across the region. We take care of every step, from levelling and soil preparation to seeding and aftercare.</p>
        <p>Our experienced crew uses quality seed and modern equipment, giving you a lawn that looks great and lasts.</p>
        <p>Get in touch for a free site visit and quote. We are happy to help with any size of job.</p>
      </div>
    </div>

    <section class="testimonial">
      <div class="mower" role="img" aria-label="Lawn mower on green grass"></div>
      <h3>Testimonial</h3>
      <div class="quote-box">
        <span class="quote-mark">“</span>
        <div>
          <p>Our new lawn came up thick and green within weeks. The team were friendly, tidy and on time. Highly recommended to anyone wanting a great lawn.</p>
          <div style="display:flex;gap:6px;margin-top:4px;align-items:center">
            <div class="avatar" role="img" aria-label="Customer portrait"></div>
            <p class="who">Jan Smith, Homeowner<br><span style="font-weight:400;color:var(--muted)">Auckland</span></p>
          </div>
        </div>
      </div>
    </section>
  </div>

  <div class="grass" role="img" aria-label="Close-up band of green grass blades"></div>

  <footer class="site-footer">
    <div class="wrap">
      <ul class="footer-links">
        <li>Home</li><li>About Us</li><li>Services</li><li>Lawn Care</li><li>Grass Seeding</li><li>Hydroseeding</li><li>Before &amp; After</li><li>FAQs</li><li>Contact</li>
      </ul>
      <div class="footer-brand"><span class="brand-square"></span><span class="brand-name">Turf Tidings</span></div>
      <div class="quote-form">
        <h4>Get a Quote For Your New Lawn!<br>Fill in the Form or Phone Us On 0800 12 34 56</h4>
        <p class="note">We will reply within one working day.</p>
        <div class="form-row"><span class="field"></span><span class="field"></span></div>
        <div class="form-row"><span class="field"></span><span class="field"></span></div>
        <div class="form-row"><span class="field tall"></span><span class="send">SEND</span></div>
      </div>
    </div>
    <div class="copyright">Copyright © Turf Tidings. All rights reserved.</div>
  </footer>

</div>
</body>
</html>
```